Tulip Orchard Wares webdesign + corecommerce implementation

Hi there!
We are a brand new small company located in central Europe, specializing in handmade coffee and tea mugs - please check www.tuliporchardwares.com

We are looking for a complete redesign, something easy, nothing complicated.

1. web desing (smooth and easy - homepage,product detail page, etc...)
2. html/css
3. corecommerce platform implementation

```html
<!DOCTYPE html>
<html lang="en">
<head>
<meta charset="utf-8">
<title>Tulip Orchard Wares</title>
<link href="https://fonts.googleapis.com/css2?family=Oswald:wght@400;500&family=Arimo:wght@400;700&display=swap" rel="stylesheet">
<style>
:root{
  --brown-dark:#6b4423;
  --beige:#f3e6cc;
  --gold:#b5852f;
  --gold-dark:#8a5e1f;
  --gold-light:#c99a45;
  --page:#f9f0ea;
  --price:#a8702b;
  --text:#6d6d6d;
  --footer:#3b3b3b;
  --card-border:#e3d9d2;
}
*{box-sizing:border-box;margin:0;padding:0}
html,body{width:900px;height:1200px;overflow:hidden}
body{background:var(--page);font-family:"Arimo",Arial,sans-serif;position:relative}
.top-bar{height:19px;background:var(--brown-dark);color:#fff;font-size:7.5px;font-weight:700;padding:6px 0 0 91px;letter-spacing:.2px}
.top-bar .login{color:#c6d13a}
.header{height:105px;background:var(--beige);position:relative}
.brand{position:absolute;left:91px;top:40px;display:flex;align-items:center;gap:10px}
.brand-mark{width:18px;height:18px;border-radius:50%;background:var(--brown-dark)}
.brand-name{font-family:"Arimo",sans-serif;font-size:24px;color:var(--brown-dark)}
.cart-box{position:absolute;left:628px;top:12px;width:180px;height:39px;background:var(--gold);display:flex;align-items:center;padding-left:12px;font-family:"Oswald",sans-serif;font-size:10px;color:var(--brown-dark)}
.cart-box svg{margin-right:12px}
.cart-box .count{margin-left:14px}
.search{position:absolute;left:628px;top:64px;width:180px;height:23px;background:#fff}
.search svg{position:absolute;left:6px;top:6px}
.nav{height:36px;background:linear-gradient(var(--gold-light),var(--gold-dark));display:flex;padding-left:90px}
.nav a{font-family:"Oswald",sans-serif;font-size:10px;color:#fff;text-decoration:none;line-height:36px;padding:0 19px;border-right:1px solid rgba(0,0,0,.15)}
.nav a.active{background:rgba(255,255,255,.18);padding:0 19px}
.nav a:last-child{border-right:none}
.hero{position:absolute;left:90px;top:176px;width:720px;height:269px;border:1px solid #ddd;background:linear-gradient(90deg,#9a7b68 0%,#b69c86 35%,#8e8f92 60%,#a4a6a9 100%);overflow:hidden}
.hero-photo{position:absolute;left:0;top:0;width:480px;height:100%;background:linear-gradient(180deg,#77716f 0%,#8c5a45 45%,#c2ab93 100%)}
.hero-copy{position:absolute;left:504px;top:76px;width:203px;color:#f1ece6;font-size:9.6px;line-height:13.6px;text-align:justify}
.hero-copy h2{font-family:"Oswald",sans-serif;font-weight:500;color:#9a532a;font-size:19px;margin-bottom:20px;text-align:left}
.hero-copy p+p{margin-top:13px}
.dots{position:absolute;left:652px;top:241px;display:flex;gap:2px}
.dots i{width:5px;height:5px;border-radius:50%;background:#888}
.dots i:first-child{background:#444}
.section-bar{position:absolute;left:90px;width:720px;height:34px;background:linear-gradient(var(--gold-light),var(--gold-dark));font-family:"Oswald",sans-serif;font-size:14px;color:#fff;padding:6px 0 0 8px}
.arrows{position:absolute;right:12px;top:8px;display:flex;gap:1px}
.arrows span{width:15px;height:15px;background:#c9a860;border:1px solid #8a5e1f;display:flex;align-items:center;justify-content:center}
.grid{position:absolute;left:90px;display:grid;grid-template-columns:repeat(4,158px);column-gap:29.5px;row-gap:13px}
.card{width:158px;height:182px;background:#fff;border:1px solid var(--card-border);padding:15px 13px 0}
.thumb{height:87px;background:linear-gradient(180deg,#6e6b68 0%,#9d7a66 55%,#c8b49c 100%)}
.card h3{font-weight:400;font-size:8.6px;color:var(--text);text-align:center;margin-top:21px}
.buy{display:flex;align-items:center;justify-content:space-between;margin-top:10px}
.price{font-family:"Oswald",sans-serif;font-size:17px;color:var(--price)}
.add{width:80px;height:24px;background:linear-gradient(var(--gold),var(--gold-dark));color:#fff;font-family:"Oswald",sans-serif;font-size:7px;display:flex;align-items:center;gap:8px;padding-left:8px}
.footer{position:absolute;left:0;top:1156px;width:900px;height:44px;background:var(--footer);color:#eee;font-size:8px;padding:19px 0 0 89px}
.social{position:absolute;left:724px;top:10px;display:flex;gap:6px}
.social i{width:24px;height:24px;border-radius:50%}
</style>
</head>
<body>
<div class="top-bar">WISH LIST (0) &nbsp;|&nbsp; MY ACCOUNT &nbsp;|&nbsp; SHOPPING CART &nbsp;|&nbsp; CHECKOUT | <span class="login">LOGIN</span></div>
<header class="header">
  <div class="brand"><span class="brand-mark"></span><span class="brand-name">Tulip Orchard Wares</span></div>
  <div class="cart-box">
    <svg width="24" height="20" viewBox="0 0 24 20"><path d="M1 2h4l3 11h12l3-8H7" fill="none" stroke="#6b4423" stroke-width="2.4"/><circle cx="9" cy="17" r="2" fill="#6b4423"/><circle cx="19" cy="17" r="2" fill="#6b4423"/></svg>
    SHOPPING CART:<span class="count">0 items</span>
  </div>
  <div class="search"><svg width="11" height="11" viewBox="0 0 11 11"><circle cx="4.5" cy="4.5" r="3.2" fill="none" stroke="#aaa" stroke-width="1.4"/><path d="M7 7l3.5 3.5" stroke="#aaa" stroke-width="1.6"/></svg></div>
</header>
<nav class="nav">
  <a class="active">HOME</a><a>CATEGORIES</a><a>NEW ARRIVALS</a><a>ABOUT OUR MUGS</a><a>MY ACCOUNT</a><a>CONTACT US</a>
</nav>

<section class="hero">
  <div class="hero-photo" role="img" aria-label="Three handpainted terracotta cups with flowers on a woven mat"></div>
  <div class="hero-copy">
    <h2>"MUG THE MOMENT"!</h2>
    <p>Hey coffee lovers! Looking for aunique coffee mug? We offer beautifulhandmade coffee mugs and tea cups bornin the heart of Europe. Beautiful design,</p>
    <p>precise execution and piece of a heart.</p>
  </div>
  <div class="dots"><i></i><i></i><i></i></div>
</section>

<div class="section-bar" style="top:461px">FEATURED PRODUCTS
  <div class="arrows"><span><svg width="6" height="8"><path d="M5 1L1 4l4 3" fill="none" stroke="#5a3a14" stroke-width="1.5"/></svg></span><span><svg width="6" height="8"><path d="M1 1l4 3-4 3" fill="none" stroke="#5a3a14" stroke-width="1.5"/></svg></span></div>
</div>

<div class="grid" style="top:510px">
  <div class="card"><div class="thumb" role="img" aria-label="Sugar bowl with meadow flowers"></div><h3>Sugar bowl with meadow flowers</h3><div class="buy"><span class="price">$28.00</span><span class="add"><svg width="14" height="11" viewBox="0 0 14 11"><path d="M0 1h2.5l2 6h7l2-5H4" fill="none" stroke="#fff" stroke-width="1.3"/><circle cx="5.5" cy="9.5" r="1" fill="#fff"/><circle cx="10.5" cy="9.5" r="1" fill="#fff"/></svg>ADD TO CART</span></div></div>
  <div class="card"><div class="thumb" role="img" aria-label="Terracotta mug with white flowers"></div><h3>Sugar bowl with meadow flowers</h3><div class="buy"><span class="price">$28.00</span><span class="add"><svg width="14" height="11" viewBox="0 0 14 11"><path d="M0 1h2.5l2 6h7l2-5H4" fill="none" stroke="#fff" stroke-width="1.3"/><circle cx="5.5" cy="9.5" r="1" fill="#fff"/><circle cx="10.5" cy="9.5" r="1" fill="#fff"/></svg>ADD TO CART</span></div></div>
  <div class="card"><div class="thumb" role="img" aria-label="Terracotta cup with yellow sun motif"></div><h3>Sugar bowl with meadow flowers</h3><div class="buy"><span class="price">$28.00</span><span class="add"><svg width="14" height="11" viewBox="0 0 14 11"><path d="M0 1h2.5l2 6h7l2-5H4" fill="none" stroke="#fff" stroke-width="1.3"/><circle cx="5.5" cy="9.5" r="1" fill="#fff"/><circle cx="10.5" cy="9.5" r="1" fill="#fff"/></svg>ADD TO CART</span></div></div>
  <div class="card"><div class="thumb" role="img" aria-label="Terracotta bowl with white daisies"></div><h3>Sugar bowl with meadow flowers</h3><div class="buy"><span class="price">$28.00</span><span class="add"><svg width="14" height="11" viewBox="0 0 14 11"><path d="M0 1h2.5l2 6h7l2-5H4" fill="none" stroke="#fff" stroke-width="1.3"/><circle cx="5.5" cy="9.5" r="1" fill="#fff"/><circle cx="10.5" cy="9.5" r="1" fill="#fff"/></svg>ADD TO CART</span></div></div>
  <div class="card"><div class="thumb" role="img" aria-label="Cream mug with painted blue pattern"></div><h3>Sugar bowl with meadow flowers</h3><div class="buy"><span class="price">$28.00</span><span class="add"><svg width="14" height="11" viewBox="0 0 14 11"><path d="M0 1h2.5l2 6h7l2-5H4" fill="none" stroke="#fff" stroke-width="1.3"/><circle cx="5.5" cy="9.5" r="1" fill="#fff"/><circle cx="10.5" cy="9.5" r="1" fill="#fff"/></svg>ADD TO CART</span></div></div>
  <div class="card"><div class="thumb" role="img" aria-label="Mug with red and black zigzag pattern"></div><h3>Sugar bowl with meadow flowers</h3><div class="buy"><span class="price">$28.00</span><span class="add"><svg width="14" height="11" viewBox="0 0 14 11"><path d="M0 1h2.5l2 6h7l2-5H4" fill="none" stroke="#fff" stroke-width="1.3"/><circle cx="5.5" cy="9.5" r="1" fill="#fff"/><circle cx="10.5" cy="9.5" r="1" fill="#fff"/></svg>ADD TO CART</span></div></div>
  <div class="card"><div class="thumb" role="img" aria-label="Terracotta mug with red painted label"></div><h3>Sugar bowl with meadow flowers</h3><div class="buy"><span class="price">$28.00</span><span class="add"><svg width="14" height="11" viewBox="0 0 14 11"><path d="M0 1h2.5l2 6h7l2-5H4" fill="none" stroke="#fff" stroke-width="1.3"/><circle cx="5.5" cy="9.5" r="1" fill="#fff"/><circle cx="10.5" cy="9.5" r="1" fill="#fff"/></svg>ADD TO CART</span></div></div>
  <div class="card"><div class="thumb" role="img" aria-label="Small terracotta mug with white flowers"></div><h3>Sugar bowl with meadow flowers</h3><div class="buy"><span class="price">$28.00</span><span class="add"><svg width="14" height="11" viewBox="0 0 14 11"><path d="M0 1h2.5l2 6h7l2-5H4" fill="none" stroke="#fff" stroke-width="1.3"/><circle cx="5.5" cy="9.5" r="1" fill="#fff"/><circle cx="10.5" cy="9.5" r="1" fill="#fff"/></svg>ADD TO CART</span></div></div>
</div>

<div class="section-bar" style="top:906px">NEW PRODUCTS
  <div class="arrows"><span><svg width="6" height="8"><path d="M5 1L1 4l4 3" fill="none" stroke="#5a3a14" stroke-width="1.5"/></svg></span><span><svg width="6" height="8"><path d="M1 1l4 3-4 3" fill="none" stroke="#5a3a14" stroke-width="1.5"/></svg></span></div>
</div>

<div class="grid" style="top:955px">
  <div class="card"><div class="thumb" role="img" aria-label="Cream mug with red striped pattern"></div><h3>Sugar bowl with meadow flowers</h3><div class="buy"><span class="price">$28.00</span><span class="add"><svg width="14" height="11" viewBox="0 0 14 11"><path d="M0 1h2.5l2 6h7l2-5H4" fill="none" stroke="#fff" stroke-width="1.3"/><circle cx="5.5" cy="9.5" r="1" fill="#fff"/><circle cx="10.5" cy="9.5" r="1" fill="#fff"/></svg>ADD TO CART</span></div></div>
  <div class="card"><div class="thumb" role="img" aria-label="Pink mug with red hearts"></div><h3>Sugar bowl with meadow flowers</h3><div class="buy"><span class="price">$28.00</span><span class="add"><svg width="14" height="11" viewBox="0 0 14 11"><path d="M0 1h2.5l2 6h7l2-5H4" fill="none" stroke="#fff" stroke-width="1.3"/><circle cx="5.5" cy="9.5" r="1" fill="#fff"/><circle cx="10.5" cy="9.5" r="1" fill="#fff"/></svg>ADD TO CART</span></div></div>
  <div class="card"><div class="thumb" role="img" aria-label="Tall pink mug with heart motif"></div><h3>Sugar bowl with meadow flowers</h3><div class="buy"><span class="price">$28.00</span><span class="add"><svg width="14" height="11" viewBox="0 0 14 11"><path d="M0 1h2.5l2 6h7l2-5H4" fill="none" stroke="#fff" stroke-width="1.3"/><circle cx="5.5" cy="9.5" r="1" fill="#fff"/><circle cx="10.5" cy="9.5" r="1" fill="#fff"/></svg>ADD TO CART</span></div></div>
  <div class="card"><div class="thumb" role="img" aria-label="Sugar bowl with meadow flowers"></div><h3>Sugar bowl with meadow flowers</h3><div class="buy"><span class="price">$28.00</span><span class="add"><svg width="14" height="11" viewBox="0 0 14 11"><path d="M0 1h2.5l2 6h7l2-5H4" fill="none" stroke="#fff" stroke-width="1.3"/><circle cx="5.5" cy="9.5" r="1" fill="#fff"/><circle cx="10.5" cy="9.5" r="1" fill="#fff"/></svg>ADD TO CART</span></div></div>
</div>

<footer class="footer">© 2013 tuliporchardwares.com. All Rights Reserved.
  <div class="social"><i style="background:#3b5a9a"></i><i style="background:#2a9fd8"></i><i style="background:#d8382c"></i></div>
</footer>
</body>
</html>
```